Brenvik Publishing

I made a website myself www.brenvikpublishing-example.co.uk a few years ago but I need a new design, which I will code. One that I can be proud of, that 's sexy, to win new customers and showcase my publishing skills. This is a publishing website so I want the home page and books page to be fantastic. I have a logo already so will like the same colour scheme or thereabouts. I have current files and features that I would like to add to your creativity and experience.

Target Market(s)

Web Designers, Graphic Designers

Industry/Entity Type

Book Publisher

Number of Pages Required

5+ page

Font styles to use
Sans Serif

Colors
0255a3
ffffff
ec1f27

Requirements
Must have
• Menu and Sub Menu
• Footer
• Buy Page - Shopping Cart
• Upload feature on the submissions page
• video section on home page (how we publish books)
• Ad space section
Nice to have
• social media bar
• Zoom in page

```html
<!DOCTYPE html>
<html lang="en">
<head>
<meta charset="utf-8">
<title>Brenvik Publishing – Self-Publishing That Works</title>
<link href="https://fonts.googleapis.com/css2?family=Bree+Serif&family=Open+Sans:wght@400;600;700&family=Roboto+Condensed:wght@400;700&display=swap" rel="stylesheet">
<style>
  :root{
    --blue:#0255a3;
    --blue-dark:#0a3b8c;
    --navy:#1f3d6e;
    --red:#ec1f27;
    --white:#ffffff;
    --paper:#ecebe8;
    --grey-text:#8a8a8a;
    --ink:#2b2b2b;
  }
  *{box-sizing:border-box;margin:0;padding:0}
  html,body{width:1200px;height:3939px;overflow:hidden;background:var(--white)}
  body{position:relative;font-family:"Open Sans",Arial,sans-serif;color:var(--ink)}
  .abs{position:absolute}

  /* HERO */
  .hero{left:0;top:0;width:1200px;height:670px;
    background:linear-gradient(100deg,#d9d8d4 0%,#c9c6c0 30%,#9a8f84 55%,#6b5a4e 75%,#d5d2cc 100%)}
  .utility{top:8px;right:58px;display:flex;gap:26px}
  .main-nav{left:302px;top:47px;width:827px;height:38px;background:var(--blue);
    display:flex;justify-content:flex-end;align-items:center;gap:34px;padding-right:16px;border-radius:2px}
  .main-nav a{color:var(--white);text-decoration:none;font-family:"Roboto Condensed",sans-serif;font-weight:700;font-size:15px;letter-spacing:.3px}
  .brand-badge{left:87px;top:0;width:126px;height:126px;border-radius:50%;background:var(--white);
    display:flex;align-items:center;justify-content:center;text-align:center;box-shadow:0 2px 6px rgba(0,0,0,.25)}
  .brand-badge span{font-weight:700;font-size:15px;line-height:1.15;color:var(--blue)}
  .hero-ribbon{left:380px;top:292px;width:447px;height:104px;background:rgba(255,255,255,.92);
    box-shadow:0 3px 10px rgba(0,0,0,.2);text-align:center;padding-top:12px}
  .hero-ribbon h1{font-family:"Roboto Condensed",sans-serif;font-weight:700;font-size:46px;color:var(--blue);line-height:1}
  .hero-ribbon p{font-size:27px;color:var(--blue);margin-top:4px}
  .btn-submit{left:509px;top:467px;width:179px;height:48px;background:var(--red);color:var(--white);
    font-family:"Roboto Condensed",sans-serif;font-weight:700;font-size:17px;display:flex;align-items:center;justify-content:center;border-radius:3px}
  .slider-dots{left:545px;top:622px;display:flex;gap:12px}
  .slider-dots i{width:16px;height:16px;border-radius:50%;background:rgba(255,255,255,.6)}
  .slider-dots i:first-child{background:var(--blue)}

  /* INTRO */
  .intro{left:0;top:670px;width:1200px;height:328px;background:var(--paper);text-align:center}
  .intro-frame{left:315px;top:68px;width:578px;height:96px;border:2px solid #cfcdc8;border-bottom:none}
  .intro h2{position:absolute;left:0;width:1200px;top:72px;font-family:"Bree Serif",serif;font-size:40px;color:var(--blue);font-weight:400}
  .intro h3{position:absolute;left:0;width:1200px;top:118px;font-family:"Bree Serif",serif;font-size:30px;color:#222;font-weight:400}
  .intro p{position:absolute;left:180px;width:840px;top:184px;font-size:18px;line-height:29px;color:var(--grey-text)}

  /* QUICK LINKS */
  .quick-links{left:0;top:998px;width:1200px;height:310px;background:var(--blue)}
  .quick-item{top:66px;width:160px;text-align:center}
  .quick-item .ring{width:124px;height:124px;margin:0 auto;border-radius:50%;border:4px solid var(--white);display:flex;align-items:center;justify-content:center;background:rgba(0,0,0,.08)}
  .quick-item span{display:inline-block;margin-top:30px;color:var(--white);font-family:"Roboto Condensed",sans-serif;font-weight:700;font-size:25px;letter-spacing:.5px;border-bottom:3px solid var(--white);padding-bottom:2px}

  /* VIDEO */
  .video-section{left:0;top:1308px;width:1200px;height:648px;background:var(--white)}
  .video-section h2{position:absolute;top:64px;left:0;width:1200px;text-align:center;color:var(--white);font-family:"Bree Serif",serif;font-weight:400;font-size:40px}
  .video-frame{left:252px;top:149px;width:693px;height:434px;background:var(--white);padding:10px;box-shadow:0 3px 12px rgba(0,0,0,.25)}
  .video-still{width:100%;height:100%;background:linear-gradient(110deg,#3b2d25 0%,#7a6355 35%,#b59c86 55%,#5a4a40 80%,#2e2520 100%);position:relative}
  .video-play{position:absolute;left:50%;top:50%;transform:translate(-50%,-50%)}

  /* STEPS */
  .steps{left:0;top:1956px;width:1200px;height:596px;background:var(--white)}
  .steps-band{left:0;top:0;width:1200px;height:342px;background:var(--navy)}
  .steps h2{position:absolute;left:0;width:1200px;top:62px;text-align:center;color:var(--white);font-family:"Bree Serif",serif;font-weight:400;font-size:40px}
  .step-card{top:166px;width:254px;height:367px;background:#f4f3f0;box-shadow:0 2px 8px rgba(0,0,0,.2)}
  .step-card svg.head{position:absolute;left:0;top:0}
  .step-num{position:absolute;left:97px;top:-10px;width:60px;height:36px;border-radius:18px;background:var(--blue);border:2px solid var(--white);color:var(--white);font-family:"Roboto Condensed",sans-serif;font-weight:700;font-size:18px;text-align:center;line-height:32px}
  .step-card h4{position:absolute;left:0;width:254px;top:32px;text-align:center;color:var(--white);font-family:"Roboto Condensed",sans-serif;font-weight:700;font-size:27px}
  .step-icon{position:absolute;left:102px;top:88px}
  .step-card p{position:absolute;left:22px;width:210px;top:187px;font-size:14px;line-height:21px;color:#555;text-align:center}

  /* PARTNERS */
  .partners{left:0;top:2552px;width:1200px;height:211px;background:#e9e8e6}
  .partners h2{position:absolute;left:0;width:1200px;top:22px;text-align:center;font-family:"Bree Serif",serif;font-weight:400;font-size:32px;color:#222}
  .partner-badge{top:90px;width:157px;height:94px;background:var(--white);border:1px solid #d9d8d4;display:flex;align-items:center;justify-content:center}
  .partner-badge i{display:block;width:96px;height:30px;border-radius:4px;background:#d7dbe2}

  /* OUR WORK */
  .our-work{left:0;top:2763px;width:1200px;height:551px;background:linear-gradient(180deg,#f2f2f2 0%,#dcdcdc 60%,#cfcfcf 100%)}
  .work-panel{left:74px;top:99px;width:1055px;height:368px;background:var(--blue);box-shadow:0 10px 18px rgba(0,0,0,.25)}
  .work-tab{left:420px;top:68px;width:357px;height:60px;background:var(--blue);border-radius:6px 6px 0 0}
  .work-tab h2{text-align:center;color:var(--white);font-family:"Bree Serif",serif;font-weight:400;font-size:40px;line-height:64px}
  .book{top:160px;width:233px;height:281px;background:var(--white);padding:12px 18px}
  .book div{width:100%;height:100%}
  .arrow-btn{width:30px;height:30px;border-radius:50%;background:var(--blue);border:2px solid var(--white);display:flex;align-items:center;justify-content:center}

  /* TESTIMONIALS */
  .testimonials{left:0;top:3314px;width:1200px;height:399px;background:var(--white)}
  .testimonials h2{position:absolute;left:92px;top:60px;font-weight:700;font-size:29px;color:#222}
  .quote-box{left:110px;top:121px;width:701px;height:215px;background:#eceae6}
  .avatar{left:21px;top:34px;width:116px;height:116px;border-radius:50%;background:linear-gradient(160deg,#b9a08a,#6f5c4e)}
  .quote-box p{position:absolute;left:184px;top:66px;width:480px;font-size:19px;line-height:27px;color:#555}
  .quote-arrow{top:217px;width:24px;height:24px;background:#555;display:flex;align-items:center;justify-content:center}
  .ad-space{left:848px;top:63px;width:276px;height:273px;background:linear-gradient(90deg,#7a1f24 0%,#a3343a 40%,#f1ede7 50%,#f5f2ee 100%);overflow:hidden}
  .ad-copy{position:absolute;left:146px;top:24px;width:124px;text-align:center;font-family:"Bree Serif",serif;color:#333}
  .ad-copy .small{font-size:14px;letter-spacing:2px}
  .ad-copy .big{font-size:22px;line-height:24px;margin-top:6px}
  .ad-copy .brand{margin-top:18px;font-family:"Open Sans",sans-serif;font-weight:700;font-size:13px;letter-spacing:1px}
  .ad-copy .shop{margin:22px auto 0;width:106px;height:28px;background:#3a9a9a;color:var(--white);font-family:"Open Sans",sans-serif;font-size:13px;line-height:28px}
  .ad-copy .url{margin-top:16px;font-family:"Open Sans",sans-serif;font-size:8px;color:#555}

  /* FOOTER */
  .site-footer{left:0;top:3713px;width:1200px;height:226px;background:var(--blue-dark)}
  .footer-brand{left:215px;top:21px;width:132px;height:132px;border-radius:50%;background:var(--white);display:flex;align-items:center;justify-content:center;text-align:center}
  .footer-brand span{font-weight:700;font-size:16px;line-height:1.15;color:var(--blue)}
  .footer-col{top:52px;display:flex;flex-direction:column;gap:7px}
  .footer-col a{color:var(--white);text-decoration:none;font-size:15px;line-height:19px}
  .stay h5{color:var(--white);font-family:"Roboto Condensed",sans-serif;font-weight:700;font-size:13px;letter-spacing:.3px}
  .social{display:flex;gap:8px;margin-top:18px}
  .social i{display:block;width:34px;height:34px;background:rgba(255,255,255,.22);border:1px solid rgba(255,255,255,.35)}
  .footer-rule{left:74px;top:176px;width:1055px;height:1px;background:rgba(255,255,255,.2)}
  .copyright{left:0;top:192px;width:1200px;text-align:center;color:var(--white);font-size:13px}
</style>
</head>
<body>

<header class="hero abs" role="img" aria-label="Photograph of a smiling woman working on a laptop">
  <div class="utility abs">
    <svg width="24" height="24" viewBox="0 0 24 24" fill="none" stroke="#333" stroke-width="2.5"><circle cx="10" cy="10" r="7"/><path d="M15 15l6 6"/></svg>
    <svg width="24" height="24" viewBox="0 0 24 24" fill="none" stroke="#333" stroke-width="2.2"><path d="M4 8h16l-1 13H5z"/><path d="M8 8V6a4 4 0 018 0v2"/></svg>
  </div>
  <nav class="main-nav abs">
    <a href="#">HOME</a><a href="#">PUBLISHING</a><a href="#">SUBMISSIONS</a><a href="#">BOOKS</a><a href="#">AUTHORS</a><a href="#">SEMINARES</a><a href="#">CONTACT US</a>
  </nav>
  <div class="brand-badge abs"><span>Brenvik<br>Publishing</span></div>
  <div class="hero-ribbon abs">
    <h1>BRENVIK PUBLISHING</h1>
    <p>Self-Publishing That Works</p>
  </div>
  <div class="btn-submit abs">SUBMIT BOOK</div>
  <div class="slider-dots abs"><i></i><i></i><i></i><i></i></div>
</header>

<section class="intro abs">
  <div class="intro-frame abs"></div>
  <h2>Have a story to tell?</h2>
  <h3>We can help you publish your book.</h3>
  <p>Welcome to Brenvik Publishing, we are an independent publishing company located in London/Surrey. We publish Trade (fiction and non-fiction), &amp; Young Adult (YA) in a variety of subjects.</p>
</section>

<section class="quick-links abs">
  <div class="quick-item abs" style="left:295px">
    <div class="ring"><svg width="62" height="56" viewBox="0 0 62 56" fill="#fff"><rect x="4" y="4" width="54" height="12" rx="3"/><rect x="8" y="20" width="50" height="12" rx="3"/><rect x="4" y="36" width="54" height="14" rx="3"/><rect x="12" y="8" width="40" height="3" fill="#0255a3"/><rect x="16" y="24" width="38" height="3" fill="#0255a3"/><rect x="12" y="41" width="40" height="3" fill="#0255a3"/></svg></div>
    <span>BOOKS</span>
  </div>
  <div class="quick-item abs" style="left:520px">
    <div class="ring"><svg width="54" height="60" viewBox="0 0 54 60" fill="#fff"><circle cx="27" cy="17" r="13"/><path d="M4 58c0-16 10-26 23-26s23 10 23 26z"/></svg></div>
    <span>AUTHORS</span>
  </div>
  <div class="quick-item abs" style="left:742px">
    <div class="ring"><svg width="60" height="54" viewBox="0 0 60 54" fill="#fff"><path d="M4 16h20v7H11v22h34v-8h7v15H4z"/><path d="M34 4l22 16-22 16v-9c-10 0-16 3-20 10 1-13 8-20 20-21z"/></svg></div>
    <span>SUBMMISION</span>
  </div>
</section>

<section class="video-section abs">
  <svg class="abs" style="left:0;top:0" width="1200" height="300" viewBox="0 0 1200 300"><polygon points="0,0 1200,0 1200,282 945,200 252,200 0,282" fill="#ec1f27"/></svg>
  <h2>Learn How We Publish Books</h2>
  <div class="video-frame abs">
    <div class="video-still" role="img" aria-label="Video still of two women talking in a café">
      <svg class="video-play" width="76" height="76" viewBox="0 0 76 76"><circle cx="38" cy="38" r="34" fill="rgba(0,0,0,.25)" stroke="#fff" stroke-width="5"/><polygon points="30,22 56,38 30,54" fill="#fff"/></svg>
    </div>
  </div>
</section>

<section class="steps abs">
  <div class="steps-band abs"></div>
  <h2>Publish Your Book in 4 Easy Steps</h2>

  <article class="step-card abs" style="left:74px">
    <svg class="head" width="254" height="165" viewBox="0 0 254 165"><polygon points="0,0 254,0 254,120 127,165 0,120" fill="#0255a3"/></svg>
    <div class="step-num">01.</div>
    <h4>WRITING</h4>
    <svg class="step-icon" width="50" height="50" viewBox="0 0 50 50" fill="none" stroke="#fff" stroke-width="2.5"><path d="M10 40l4-12 22-22 8 8-22 22z"/><path d="M14 28l8 8"/></svg>
    <p>You write a book to the best of your ability And after redrafting several times when you honestly feel that you have done the best you Possibly can with it, you send it to us</p>
  </article>

  <article class="step-card abs" style="left:344px">
    <svg class="head" width="254" height="165" viewBox="0 0 254 165"><polygon points="0,0 254,0 254,120 127,165 0,120" fill="#0255a3"/></svg>
    <div class="step-num">02.</div>
    <h4>SUBMISSION</h4>
    <svg class="step-icon" width="50" height="50" viewBox="0 0 50 50" fill="none" stroke="#fff" stroke-width="2.5"><path d="M12 6h18l10 10v28H12z"/><path d="M30 6v10h10"/><path d="M26 38V24m-6 6l6-6 6 6"/></svg>
    <p>If your book is in our subject matter and you think you have something that could tickle our fancy, send Us your book for review.</p>
  </article>

  <article class="step-card abs" style="left:614px">
    <svg class="head" width="254" height="165" viewBox="0 0 254 165"><polygon points="0,0 254,0 254,120 127,165 0,120" fill="#0255a3"/></svg>
    <div class="step-num">03.</div>
    <h4>REVIEW</h4>
    <svg class="step-icon" width="50" height="50" viewBox="0 0 50 50" fill="none" stroke="#fff" stroke-width="2.5"><polygon points="25,5 31,18 45,19 34,28 38,42 25,34 12,42 16,28 5,19 19,18"/></svg>
    <p>You send us your book and our editorial team will look over it and decide if we like it and</p>
  </article>

  <article class="step-card abs" style="left:882px">
    <svg class="head" width="254" height="165" viewBox="0 0 254 165"><polygon points="0,0 254,0 254,120 127,165 0,120" fill="#0255a3"/></svg>
    <div class="step-num">04.</div>
    <h4>CONTRACT</h4>
    <svg class="step-icon" width="50" height="50" viewBox="0 0 50 50" fill="none" stroke="#fff" stroke-width="2.5"><rect x="11" y="8" width="28" height="36" rx="2"/><rect x="19" y="4" width="12" height="7" fill="#0255a3"/><path d="M17 20h16M17 27h16M17 34h10"/></svg>
    <p>You send us your book and our editorial team will look over it and decide if we like it and then we will Decide what</p>
  </article>
</section>

<section class="partners abs">
  <h2>Companies We Work With</h2>
  <div class="partner-badge abs" style="left:92px"><i></i></div>
  <div class="partner-badge abs" style="left:265px"><i></i></div>
  <div class="partner-badge abs" style="left:438px"><i></i></div>
  <div class="partner-badge abs" style="left:611px"><i></i></div>
  <div class="partner-badge abs" style="left:784px"><i></i></div>
  <div class="partner-badge abs" style="left:956px"><i></i></div>
</section>

<section class="our-work abs">
  <div class="work-panel abs"></div>
  <div class="work-tab abs"><h2>Our Work</h2></div>
  <div class="book abs" style="left:100px"><div role="img" aria-label="Book cover: collage of food and fitness photos" style="background:linear-gradient(160deg,#e2c23a,#c8462e 45%,#3b8b5a)"></div></div>
  <div class="book abs" style="left:357px"><div role="img" aria-label="Book cover: plain black cover with white title" style="background:#1c1c1c"></div></div>
  <div class="book abs" style="left:612px"><div role="img" aria-label="Book cover: illustrated figures on a dark background" style="background:linear-gradient(180deg,#1b1f3a,#3a3358 60%,#b38a3c)"></div></div>
  <div class="book abs" style="left:866px"><div role="img" aria-label="Book cover: deep red cloth design with gold border" style="background:linear-gradient(180deg,#8c1b1f,#6e1216)"></div></div>
  <div class="arrow-btn abs" style="left:61px;top:212px"><svg width="12" height="12" viewBox="0 0 12 12"><path d="M8 1L3 6l5 5" stroke="#fff" stroke-width="2" fill="none"/></svg></div>
  <div class="arrow-btn abs" style="left:1107px;top:212px"><svg width="12" height="12" viewBox="0 0 12 12"><path d="M4 1l5 5-5 5" stroke="#fff" stroke-width="2" fill="none"/></svg></div>
</section>

<section class="testimonials abs">
  <h2>Testimonials</h2>
  <div class="quote-box abs">
    <div class="avatar abs" role="img" aria-label="Portrait photo of the reviewer"></div>
    <p>"You send us your book and our editorial team will look over it and decide if we like it and then we will Decide what."</p>
  </div>
  <div class="quote-arrow abs" style="left:80px"><svg width="10" height="10" viewBox="0 0 10 10"><polygon points="7,1 2,5 7,9" fill="#fff"/></svg></div>
  <div class="quote-arrow abs" style="left:795px"><svg width="10" height="10" viewBox="0 0 10 10"><polygon points="3,1 8,5 3,9" fill="#fff"/></svg></div>
  <aside class="ad-space abs" role="img" aria-label="Advertisement: photo of a wooden wristwatch">
    <div class="ad-copy">
      <div class="small">LUXURY</div>
      <div class="big">WOOD<br>WATCHES</div>
      <div class="brand">TIMBERLINE</div>
      <div class="shop">SHOP NOW</div>
      <div class="url">TIMBERLINE-EXAMPLE.COM</div>
    </div>
  </aside>
</section>

<footer class="site-footer abs">
  <div class="footer-brand abs"><span>Brenvik<br>Publishing</span></div>
  <div class="footer-col abs" style="left:394px"><a href="#">Submissions</a><a href="#">Production</a><a href="#">Ebooks</a></div>
  <div class="footer-col abs" style="left:549px"><a href="#">Books</a><a href="#">Seminars</a><a href="#">Packages</a></div>
  <div class="footer-col abs" style="left:675px"><a href="#">Authors</a><a href="#">Contact</a><a href="#">Career</a></div>
  <div class="stay abs" style="left:788px;top:56px">
    <h5>STAY CONNECTED</h5>
    <div class="social"><i></i><i></i><i></i><i></i><i></i></div>
  </div>
  <div class="footer-rule abs"></div>
  <div class="copyright abs">© 2016 Brenvik Publishing. All Rights Reserved.</div>
</footer>

</body>
</html>
```